Business card for a new cabinet shop company named Marlowe Cabinets for high end cabinets

Design a business card, thinking dark rich green with colours to speak of high end luxury ie; cream, gold, black possibly

Peter Lindqvar
Director Craftsman
Email: info@marlowecabinets.com.au
Instagram : @marlowe.cabinets

```html
<!DOCTYPE html>
<html lang="en">
<head>
<meta charset="utf-8">
<title>Marlowe Cabinets – Business Card</title>
<link rel="stylesheet" href="https://fonts.googleapis.com/css2?family=Arimo:wght@400;700&display=swap">
<style>
  :root {
    --backdrop: #3b3b3d;
    --card: #f4f4f2;
    --gold: #b99a52;
    --ink: #111111;
    --muted: #6b6b6b;
    --rule: #555555;
  }
  * { box-sizing: border-box; margin: 0; padding: 0; }
  html, body {
    width: 1200px;
    height: 900px;
    overflow: hidden;
    background: var(--backdrop);
    font-family: "Arimo", Arial, sans-serif;
  }
  .stage {
    width: 1200px;
    height: 900px;
    display: flex;
    flex-direction: column;
    align-items: center;
    justify-content: center;
    gap: 50px;
  }
  .card {
    width: 630px;
    height: 360px;
    background: var(--card);
    border-radius: 40px;
    box-shadow: 0 14px 30px rgba(0,0,0,0.45);
    position: relative;
    display: flex;
    align-items: center;
  }
  .card--front { justify-content: center; }

  .brand {
    display: flex;
    align-items: center;
    gap: 16px;
  }
  .brand__mark {
    width: 46px;
    height: 46px;
    border: 3px solid var(--ink);
    flex: none;
  }
  .brand__name {
    font-family: "Arimo", Arial, sans-serif;
    font-weight: 400;
    font-size: 30px;
    color: var(--gold);
    letter-spacing: 0.5px;
    line-height: 1.1;
    width: 170px;
  }

  .card--back { padding-left: 60px; }
  .card--back .brand__name { font-size: 27px; width: 150px; }
  .divider {
    width: 1px;
    height: 120px;
    background: var(--rule);
    margin: 0 26px 0 34px;
  }
  .contact { display: flex; flex-direction: column; }
  .contact__name {
    font-weight: 700;
    font-size: 19px;
    color: var(--ink);
    text-transform: uppercase;
    letter-spacing: 0.2px;
  }
  .contact__role {
    font-size: 15px;
    color: var(--muted);
    margin-top: 3px;
  }
  .contact__list {
    list-style: none;
    margin-top: 22px;
    display: flex;
    flex-direction: column;
    gap: 5px;
  }
  .contact__item {
    display: flex;
    align-items: center;
    gap: 8px;
    font-size: 15px;
    color: var(--muted);
  }
  .contact__icon { width: 14px; height: 14px; flex: none; }
</style>
</head>
<body>
  <main class="stage">
    <section class="card card--front" aria-label="Card front">
      <div class="brand">
        <span class="brand__mark"></span>
        <span class="brand__name">Marlowe Cabinets</span>
      </div>
    </section>

    <section class="card card--back" aria-label="Card back">
      <div class="brand">
        <span class="brand__mark"></span>
        <span class="brand__name">Marlowe Cabinets</span>
      </div>
      <span class="divider"></span>
      <div class="contact">
        <p class="contact__name">Peter Lindqvar</p>
        <p class="contact__role">Director Craftsman</p>
        <ul class="contact__list">
          <li class="contact__item">
            <svg class="contact__icon" viewBox="0 0 14 14" aria-hidden="true">
              <circle cx="7" cy="7" r="6.5" fill="var(--gold)"/>
            </svg>
            @marlowe.cabinets
          </li>
          <li class="contact__item">
            <svg class="contact__icon" viewBox="0 0 14 14" aria-hidden="true">
              <rect x="0.5" y="2.5" width="13" height="9" fill="var(--gold)"/>
              <path d="M0.5 2.5 L7 8 L13.5 2.5" fill="none" stroke="var(--card)" stroke-width="1.2"/>
            </svg>
            info@marlowecabinets.com.au
          </li>
        </ul>
      </div>
    </section>
  </main>
</body>
</html>
```